Revamp Current Website From 2012 TO 2018

We need a ravamp to our current website. I prefer a professional corporate modern feel to it.

My Current Website is www.brightlanepromoworks.biz. Please redesign the homepage and the /certs page first....see attached document for specific instructions..

There is a lot of content at the bottom but maybe we can shorten that by using titles and a pop up of the details or something so it doesnt take too mcuh space...or maybe a red more hyperlink to see the rest of info in pop up or something or new page...

Target Market(s)

B2B, business owners, website owners, marketing companies.

Industry/Entity Type

Promotional Product

Number of Pages Required

2 page

Colors

Designer to choose colors to be used in the design.

Requirements
Must have
• Please keep in mind logo mock up I am working on that looks beautiful on dark background for header...see attached for logo
• Must use existing content I hope your marketing mind comes in to play when designing the website.
• Must have all my content provided on each page...
Nice to have
• similiar color scheme...
Should not have
• I dont like using templates because usually hard to expand on design in future so Prefer full custom designs
• Please no templates

```html
<!DOCTYPE html>
<html lang="en">
<head>
<meta charset="utf-8">
<title>Brightlane Promo Works</title>
<link href="https://fonts.googleapis.com/css2?family=Montserrat:wght@400;500;600;700&family=Open+Sans:wght@400;600&display=swap" rel="stylesheet">
<style>
:root{
  --blue:#0b72c9;
  --dark:#141414;
  --ink:#222;
  --muted:#777;
  --light:#f1f1f1;
  --line:#d9d9d9;
  --white:#fff;
}
*{margin:0;padding:0;box-sizing:border-box}
html,body{width:1200px;height:3267px;overflow:hidden}
body{font-family:"Open Sans",Arial,sans-serif;color:var(--ink);background:var(--white);position:relative}
.abs{position:absolute}
.section-title{font-family:"Montserrat",Arial,sans-serif;font-weight:500;font-size:21px;letter-spacing:1px;text-transform:uppercase;text-align:center;color:var(--ink)}
.section-title::after{content:"";display:block;width:40px;height:3px;background:var(--blue);margin:14px auto 0}

/* hero */
.hero{position:absolute;left:0;top:0;width:1200px;height:510px;background:linear-gradient(180deg,#2b2b2b 0%,#1d1f22 45%,#3a3631 100%)}
.hero-photo{position:absolute;inset:135px 0 0 0;background:linear-gradient(90deg,rgba(30,30,30,.2),rgba(80,70,60,.35) 55%,rgba(20,20,20,.2))}
.topbar{position:absolute;left:0;top:0;width:1200px;height:44px;background:#0e0e0e}
.top-links{left:209px;top:9px;font:600 9px "Montserrat",sans-serif;color:#ddd;letter-spacing:.5px;display:flex;gap:18px}
.top-links span::before{content:"";display:inline-block;width:6px;height:6px;border-radius:50%;background:var(--blue);margin-right:5px}
.trial{left:834px;top:0;width:157px;height:30px;background:var(--blue);color:#fff;font:600 9.5px "Montserrat",sans-serif;display:flex;align-items:center;justify-content:center;letter-spacing:.5px}
.brand{left:207px;top:56px;display:flex;align-items:center;gap:8px;font:700 13px/13px "Montserrat",sans-serif;color:var(--blue)}
.brand .mark{width:20px;height:20px;border:3px solid var(--blue)}
.brand small{display:block;font:600 7px "Montserrat",sans-serif;letter-spacing:5px;color:#ccc;margin-top:2px}
.phones{left:583px;top:60px;display:flex;gap:38px;font-size:11.5px;color:#ddd}
.phones u{color:#bbb;margin-right:10px}
.nav{position:absolute;left:0;top:109px;width:1200px;height:28px;background:rgba(70,70,70,.85)}
.nav-list{list-style:none;display:flex;gap:28px;margin-left:209px;padding-top:9px;font:500 9.5px "Montserrat",sans-serif;color:#eee;letter-spacing:.4px}
.nav-list li.active{color:var(--blue)}
.hero-title{left:207px;top:198px;width:600px;font:400 21px/30px "Montserrat",sans-serif;color:#fff}
.hero-points{left:207px;top:304px;list-style:none;font-size:12.5px;line-height:23px;color:#e6e6e6}
.hero-points li::before{content:"";display:inline-block;width:5px;height:5px;background:var(--blue);margin-right:12px;vertical-align:middle}
.side{top:300px;font:600 9px "Montserrat",sans-serif;color:#888;letter-spacing:3px;writing-mode:vertical-rl}
.dots{left:584px;top:468px;display:flex;gap:6px}
.dots i{width:8px;height:8px;border-radius:50%;border:1px solid #ccc}
.dots i.on{background:#fff}

/* about */
.about{position:absolute;left:0;top:510px;width:1200px;height:403px;background:#fff}
.about-team{left:440px;top:30px;width:580px;height:373px;background:linear-gradient(90deg,#fff,#eef0f2 30%,#f1f2f4 70%,#fff)}
.about-person{left:664px;top:52px;width:229px;height:351px;background:linear-gradient(180deg,#c7a58e 0%,#b9cce0 40%,#9bb3cf 100%);border-radius:90px 90px 0 0}
.about-title{left:248px;top:124px;width:332px}
.about-text{left:258px;top:178px;width:312px;text-align:center;font-size:11.5px;line-height:18.5px;color:#666}
.btn{background:var(--blue);color:#fff;font:600 10px "Montserrat",sans-serif;letter-spacing:.6px;display:flex;align-items:center;justify-content:center}
.about-btn{left:348px;top:302px;width:127px;height:29px}

/* ways */
.ways{position:absolute;left:0;top:913px;width:1200px;height:670px;background:var(--light)}
.ways-title{left:300px;top:67px;width:600px;line-height:30px}
.timeline{left:599px;top:202px;width:1px;height:388px;background:var(--line)}
.way h3{font:600 14px/20px "Montserrat",sans-serif;color:var(--ink)}
.way p{font-size:11px;line-height:18.5px;color:#777;margin-top:12px}
.num{font:500 38px "Montserrat",sans-serif;color:var(--blue)}
.node{width:9px;height:9px;border:1px solid var(--blue);border-radius:50%;background:var(--light)}

/* distribution */
.dist{position:absolute;left:0;top:1583px;width:1200px;height:436px;background:#fff}
.dist-title{left:300px;top:52px;width:600px}
.channel{top:155px;width:200px;text-align:center}
.channel .ico{width:87px;height:87px;border-radius:50%;background:#5a5d62;margin:0 auto;display:flex;align-items:center;justify-content:center}
.channel.active .ico{background:var(--blue)}
.channel h3{font:600 15px "Montserrat",sans-serif;margin-top:25px}
.channel p{width:165px;margin:8px auto 0;font-size:11px;line-height:18.5px;color:#777;height:58px}
.channel a{font:600 10px "Montserrat",sans-serif;color:var(--blue);text-decoration:none}

/* testimonial */
.quote{position:absolute;left:0;top:2019px;width:1200px;height:399px;background:linear-gradient(100deg,#101010,#2a2a2a 50%,#141414)}
.quote-bg{inset:0;background:linear-gradient(115deg,rgba(255,255,255,.03),rgba(255,255,255,.08) 50%,rgba(255,255,255,.02))}
.quote-text{left:350px;top:120px;width:500px;text-align:center;font-size:11.5px;line-height:19px;color:#ddd}
.avatars{left:0;top:225px;width:1200px;display:flex;justify-content:center;align-items:center;gap:14px}
.avatars span{width:52px;height:52px;border-radius:50%;background:#6b6b6b;border:2px solid #999}
.avatars span.main{width:72px;height:72px;background:#8a8a8a;border-color:#fff}
.who{left:0;top:311px;width:1200px;text-align:center;font-size:11px;color:#ddd}
.who b{display:block;color:var(--blue);font-weight:600}

/* clients */
.clients{position:absolute;left:0;top:2418px;width:1200px;height:300px;background:#fff}
.clients-title{left:300px;top:70px;width:600px}
.client{top:157px;width:114px;height:69px;background:#e7e7e7;display:flex;align-items:center;justify-content:center;font:600 12px "Montserrat",sans-serif;color:#333}

/* newsletter */
.news{position:absolute;left:0;top:2718px;width:1200px;height:81px;background:var(--light)}
.news-title{left:207px;top:28px;font:500 19px "Montserrat",sans-serif;letter-spacing:1px}
.news-field{left:383px;top:27px;width:451px;height:28px;background:#fff;border:1px solid #e2e2e2}
.news-btn{left:847px;top:27px;width:144px;height:28px}

/* footer */
.footer{position:absolute;left:0;top:2799px;width:1200px;height:468px;background:#000;color:#ddd}
.footer-title{left:300px;top:64px;width:600px;color:#fff}
.col{top:168px;width:270px;text-align:center;font-size:11.5px;line-height:17px}
.col svg{display:block;margin:0 auto 16px}
.col b{display:block;font-weight:600;color:#fff}
.divider{top:150px;width:1px;height:130px;background:#333}
.social{left:0;top:316px;width:1200px;display:flex;justify-content:center;gap:14px}
.social span{width:35px;height:35px;border-radius:50%;background:#666}
.social span.on{background:var(--blue)}
.copy{left:0;top:384px;width:1200px;text-align:center;font-size:10.5px;color:#888}
.totop{left:972px;top:352px}
</style>
</head>
<body>

<section class="hero">
  <div class="hero-photo abs" role="img" aria-label="Blurred photo of a busy city street behind the headline"></div>
  <div class="topbar">
    <div class="top-links abs"><span>LOGIN</span><span>SIGN UP</span></div>
    <div class="trial abs">TRY FOR 30 DAYS →</div>
  </div>
  <div class="brand abs"><div class="mark"></div><div>BRIGHTLANE PROMO<small>WORKS</small></div></div>
  <div class="phones abs">
    <div><u>USA Office</u>☎ 555-204-7731</div>
    <div><u>International</u>☎ 1-800-555-0148</div>
  </div>
  <nav class="nav"><ul class="nav-list">
    <li class="active">HOME</li><li>OUR INCENTIVES</li><li>SAMPLES</li><li>HOW IT WORKS</li><li>TESTIMONIALS</li><li>FAQ</li><li>CONTACT</li>
  </ul></nav>
  <h1 class="hero-title abs">Increase Leads &amp; Sales From Your Existing<br>Marketing Efforts By Offering High Perceived Value<br>Incentives To Your Customers!</h1>
  <ul class="hero-points abs">
    <li>12 Years In Business</li>
    <li>13,000+ Clients Enrolled</li>
    <li>2+ Million Certificates In Circulation</li>
    <li>170,000+ Redemptions To Date</li>
    <li>A+ Service Rating</li>
    <li>Licensed Seller Of Travel CST #4470318</li>
  </ul>
  <div class="side abs" style="left:52px">PREV</div>
  <div class="side abs" style="left:1134px">NEXT</div>
  <div class="dots abs"><i class="on"></i><i></i><i></i></div>
</section>

<section class="about">
  <div class="about-team abs" role="img" aria-label="Faded photo of a business team in the background"></div>
  <div class="about-person abs" role="img" aria-label="Photo of a smiling businessman with arms crossed"></div>
  <h2 class="section-title about-title abs">About Us</h2>
  <p class="about-text abs">Create a variety giveaway promotions for your business with an unlimited supply of top quality vacation getaway certificates, restaurant gift certificates, electronic product giveaways and gas or grocery rewards for just $99/mth. Whether you need 100 or 100,000 you will never pay more than $99.</p>
  <div class="btn about-btn abs">READ MORE →</div>
</section>

<section class="ways">
  <h2 class="section-title ways-title abs">We plug right into your existing<br>business model in 4 ways</h2>
  <div class="timeline abs"></div>

  <div class="way abs" style="left:231px;top:229px;width:225px">
    <h3>Boost Response Rates To Your Existing Ads</h3>
    <p>By adding one extra tagline: "Call for a Free Quote and receive a Three Day Two Night Hotel Stay Certificate to Las Vegas or 50 + other popular destinations, No Purchase Necessary." Imagine how many more leads you could generate.</p>
  </div>
  <div class="num abs" style="left:486px;top:222px">01</div>
  <div class="node abs" style="left:550px;top:243px"></div>

  <div class="num abs" style="left:664px;top:341px">02</div>
  <div class="node abs" style="left:634px;top:362px"></div>
  <div class="way abs" style="left:749px;top:352px;width:310px">
    <h3>Get More New Customers</h3>
    <p>Now that you have generated a new lead, try enticing them with an upgrade and offer them Two Nights Plus Airfare if they purchase today.</p>
  </div>

  <div class="way abs" style="left:231px;top:456px;width:225px">
    <h3>Increase Repeat &amp; Referral Business</h3>
    <p>Remind past clients about your products &amp; services with a 7 Night Resort Getaway in one of over 3500 destinations around the world to motivate repeat business and to anyone who fulfills your request for a new referral.</p>
  </div>
  <div class="num abs" style="left:486px;top:449px">03</div>
  <div class="node abs" style="left:550px;top:470px"></div>
</section>

<section class="dist">
  <h2 class="section-title dist-title abs">Easy Distribution</h2>
  <div class="channel abs" style="left:199px">
    <div class="ico"><svg width="40" height="40" viewBox="0 0 40 40" fill="none" stroke="#fff" stroke-width="2"><rect x="11" y="6" width="18" height="9"/><rect x="5" y="15" width="30" height="13" rx="2"/><rect x="11" y="24" width="18" height="10" fill="#5a5d62"/></svg></div>
    <h3>Print</h3>
    <p>Download PDF certificates to print and physically hand them</p>
    <a>Read More →</a>
  </div>
  <div class="channel abs active" style="left:399px">
    <div class="ico"><svg width="40" height="40" viewBox="0 0 40 40" fill="none" stroke="#fff" stroke-width="2"><path d="M5 16 L20 5 L35 16 V34 H5 Z"/><path d="M5 16 L20 26 L35 16"/><rect x="11" y="10" width="18" height="11"/></svg></div>
    <h3>Email</h3>
    <p>Email e-certificates to your customers individually or in bulk with</p>
    <a>Read More →</a>
  </div>
  <div class="channel abs" style="left:604px">
    <div class="ico"><svg width="40" height="40" viewBox="0 0 40 40" fill="none" stroke="#fff" stroke-width="2"><path d="M12 24 A7 7 0 0 1 13 11 A9 9 0 0 1 30 13 A6 6 0 0 1 29 24 Z"/><path d="M20 24 V34 M14 27 V33 M26 27 V33"/></svg></div>
    <h3>Online Animation</h3>
    <p>Add our web banners on your website. Your customers click on the banne</p>
    <a>Read More →</a>
  </div>
  <div class="channel abs" style="left:809px">
    <div class="ico"><svg width="40" height="40" viewBox="0 0 40 40" fill="none" stroke="#fff" stroke-width="2"><path d="M20 7 C29 7 35 12 35 19 C35 26 29 31 20 31 L11 35 L13 28 C8 26 5 23 5 19 C5 12 11 7 20 7 Z"/><circle cx="14" cy="19" r="1.5" fill="#fff"/><circle cx="20" cy="19" r="1.5" fill="#fff"/><circle cx="26" cy="19" r="1.5" fill="#fff"/></svg></div>
    <h3>Sms</h3>
    <p>Send sms-certificates through text messaging with just one click!</p>
    <a>Read More →</a>
  </div>
</section>

<section class="quote">
  <div class="quote-bg abs" role="img" aria-label="Dark scattered travel certificates in the background"></div>
  <svg class="abs" style="left:580px;top:62px" width="40" height="32" viewBox="0 0 40 32" fill="#0b72c9"><path d="M0 32 V18 C0 8 5 2 15 0 L16 5 C10 7 8 10 8 14 H16 V32 Z M22 32 V18 C22 8 27 2 37 0 L38 5 C32 7 30 10 30 14 H38 V32 Z"/></svg>
  <svg class="abs" style="left:132px;top:192px" width="16" height="26" viewBox="0 0 16 26" fill="none" stroke="#fff" stroke-width="3"><path d="M14 2 L3 13 L14 24"/></svg>
  <svg class="abs" style="left:1048px;top:192px" width="16" height="26" viewBox="0 0 16 26" fill="none" stroke="#fff" stroke-width="3"><path d="M2 2 L13 13 L2 24"/></svg>
  <p class="quote-text abs">There are many variations of passages of Lorem Ipsum available, but the majority have suffered alteration in some form, by injected humour, or randomised words which don't look even slightly believable. If you are going to use a passage of Lorem Ipsum, you need to be sure there isn't anything embarrassing hidden....</p>
  <div class="avatars abs">
    <span role="img" aria-label="Client portrait"></span>
    <span class="main" role="img" aria-label="Client portrait"></span>
    <span role="img" aria-label="Client portrait"></span>
  </div>
  <div class="who abs"><b>Dana Ellis</b>General Manager</div>
</section>

<section class="clients">
  <h2 class="section-title clients-title abs">Our Clients</h2>
  <div class="client abs" style="left:274px">Northgate Realty</div>
  <div class="client abs" style="left:453px">HomeCart</div>
  <div class="client abs" style="left:632px">Veloro Motors</div>
  <div class="client abs" style="left:810px">SkyCast</div>
</section>

<section class="news">
  <h3 class="news-title abs">NEWS LETTER</h3>
  <div class="news-field abs"></div>
  <div class="btn news-btn abs">SUBSCRIBE NOW</div>
</section>

<footer class="footer">
  <h2 class="section-title footer-title abs">Contact Us</h2>
  <div class="col abs" style="left:192px">
    <svg width="36" height="36" viewBox="0 0 36 36" fill="none" stroke="#ccc" stroke-width="1.6"><path d="M8 4 L14 10 L10 15 C12 20 16 24 21 26 L26 22 L32 28 L27 33 C16 32 4 20 3 9 Z"/></svg>
    <b>Call</b>555-204-7731<br>1-800-555-0148
  </div>
  <div class="divider abs" style="left:464px"></div>
  <div class="col abs" style="left:464px">
    <svg width="36" height="36" viewBox="0 0 36 36" fill="none" stroke="#ccc" stroke-width="1.6"><path d="M18 34 C10 24 7 18 7 13 A11 11 0 0 1 29 13 C29 18 26 24 18 34 Z"/><circle cx="18" cy="13" r="4"/></svg>
    <b>Brightlane Promo Group Inc</b>1180 Harbor Row, Unit B4,<br>Millbrook, ON K0L 2A3
  </div>
  <div class="divider abs" style="left:734px"></div>
  <div class="col abs" style="left:734px">
    <svg width="44" height="36" viewBox="0 0 44 36" fill="none" stroke="#ccc" stroke-width="1.6"><rect x="3" y="6" width="38" height="25"/><path d="M3 6 L22 21 L41 6"/></svg>
    <b>E-mail Us</b>hello@brightlanepromo.biz
  </div>
  <div class="social abs">
    <span class="on" role="img" aria-label="Social profile"></span>
    <span role="img" aria-label="Social profile"></span>
    <span role="img" aria-label="Social profile"></span>
  </div>
  <div class="copy abs">© Copyright 2017 Brightlane Promo Group Inc.. All Rights Reserved</div>
  <svg class="totop abs" width="18" height="34" viewBox="0 0 18 34" fill="none" stroke="#0b72c9" stroke-width="2"><path d="M9 33 V3 M2 10 L9 2 L16 10"/></svg>
</footer>

</body>
</html>
```